Corvath Holdings, LLC

We are a design build general contracting company.
We work with commercial accounts and private developers. We build retail spaces, restaurants and housing projects.
Im looking for a clean professional type of logo incorporating a roman flavor, think ionic columns and pedestals.
Two toned colorway.
I like unusual fonts and Im not afraid to do something bold with the logo.
Contact Information for Business Card
Marisol Brenkowitz
318-472-9051 corvathmb@mailvexo.com
Font styles to use
Decorative
Colors
Designer to choose colors to be used in the design.
Requirements
Should not have
- I don't like reds pinks.

```html
<!DOCTYPE html>
<html lang="en">
<head>
<meta charset="utf-8">
<title>Corvath Holdings, LLC — Business Card</title>
<link href="https://fonts.googleapis.com/css2?family=Mulish:wght@700&family=Questrial&display=swap" rel="stylesheet">
<style>
  :root {
    --backdrop: #dcdcdc;
    --card: #f2f2f2;
    --band: #333333;
    --ink: #333333;
    --ink-soft: #4a4a4a;
    --on-band: #ffffff;
  }
  * { margin: 0; padding: 0; box-sizing: border-box; }
  html, body {
    width: 1200px; height: 960px; overflow: hidden;
    background: var(--backdrop);
  }
  .canvas { position: relative; width: 1200px; height: 960px; }
  .card {
    position: absolute; width: 600px; height: 343px;
    background: var(--card); overflow: hidden;
  }
  .card--front { left: 302px; top: 120px; }
  .card--back { left: 299px; top: 497px; }

  .band {
    position: absolute; left: 0; top: 51px; width: 100%; height: 86px;
    background: var(--band);
  }
  .holder-name {
    position: absolute; left: 51px; top: 28px;
    font-family: "Mulish", sans-serif; font-weight: 700; font-size: 22px;
    color: var(--on-band); letter-spacing: 0.2px;
  }
  .brand-mark {
    position: absolute; left: 423px; top: 24px; width: 38px; height: 38px;
    background: var(--on-band);
  }
  .company-name {
    position: absolute; left: 339px; top: 142px;
    font-family: "Mulish", sans-serif; font-weight: 700; font-size: 19px;
    color: var(--ink);
  }
  .contact-list {
    position: absolute; left: 51px; top: 238px; list-style: none;
    font-family: "Questrial", sans-serif; font-size: 15px; color: var(--ink-soft);
  }
  .contact-list li { display: flex; align-items: center; height: 19px; }
  .contact-list svg { width: 13px; height: 13px; margin-right: 9px; fill: var(--ink); }

  .back-brand {
    position: absolute; left: 0; top: 0; width: 100%; height: 100%;
    display: flex; align-items: center; justify-content: center; gap: 14px;
  }
  .back-brand__mark { width: 30px; height: 30px; background: var(--ink); }
  .back-brand__name {
    font-family: "Mulish", sans-serif; font-weight: 700; font-size: 22px; color: var(--ink);
  }
</style>
</head>
<body>
<main class="canvas">
  <section class="card card--front" aria-label="Business card front">
    <div class="band">
      <h1 class="holder-name">Marisol Brenkowitz</h1>
      <span class="brand-mark" aria-hidden="true"></span>
    </div>
    <p class="company-name">Corvath Holdings, LLC</p>
    <ul class="contact-list">
      <li>
        <svg viewBox="0 0 16 16" aria-hidden="true"><path d="M3.6 1.2l2.3 2.6-1.4 1.9c.9 2 2.3 3.5 4.3 4.6l1.9-1.4 2.7 2.3-1.3 2.6C6.6 13.7 2.1 9.3 1.1 3z"/></svg>
        318-472-9051
      </li>
      <li>
        <svg viewBox="0 0 16 16" aria-hidden="true"><path d="M1 3.5h14v1L8 9 1 4.5z M1 6l7 4.5L15 6v6.5H1z"/></svg>
        corvathmb@mailvexo.com
      </li>
      <li>
        <svg viewBox="0 0 16 16" aria-hidden="true"><path d="M8 1a7 7 0 1 0 0 14A7 7 0 0 0 8 1zm-1 2.3c-.3 1 .6 1.5.2 2.4-.5.9-1.8.6-2.1 1.7-.3 1 .8 1.6.6 2.8-.1.7-.7 1.2-1 1.9A5.3 5.3 0 0 1 7 3.3zm2.6 9.6c.2-.9 1-1.2 1-2.2 0-1.2-1.6-1.3-2.2-2.2-.5-.8.2-1.6 1-1.7.8-.1 1.5.5 2.1.2a5.3 5.3 0 0 1-1.9 5.9z"/></svg>
        www.corvathholdings.com
      </li>
    </ul>
  </section>

  <section class="card card--back" aria-label="Business card back">
    <div class="back-brand">
      <span class="back-brand__mark" aria-hidden="true"></span>
      <span class="back-brand__name">Corvath Holdings, LLC</span>
    </div>
  </section>
</main>
</body>
</html>
```